Zo Fen smart screen Flyer design

Hi,

Please see attached file as I have done up a very very basic flyer just with the information that will need to be presented.

Please don't go with this as a format I would like, as I have no design skills at all.

I'm looking for something that is basic but professional looking capturing this information.
I would prefer if the symbols were changed so they were all consistent and the colour scheme worked together with the logo.

If you can use the picture of the screen provided as I will replace this once my product has its photoshoot.

Thanks!

```html
<!DOCTYPE html>
<html lang="en">
<head>
<meta charset="utf-8">
<title>Zo Fen Smart Screen Flyer</title>
<link href="https://fonts.googleapis.com/css2?family=Raleway:wght@300;400;500&display=swap" rel="stylesheet">
<style>
:root{
  --stage:#e6e6e6;
  --paper:#ffffff;
  --sky:#29a9e0;
  --mist:#ebebeb;
  --sun:#fbdb00;
  --ink:#1d1d1b;
  --ink-soft:#3c3c3b;
  --icon:#3a3a3a;
}
*{margin:0;padding:0;box-sizing:border-box}
html,body{width:849px;height:1200px;overflow:hidden;background:var(--stage)}
body{font-family:'Raleway',sans-serif;color:var(--ink);position:relative}
.flyer{position:absolute;left:0;top:49px;width:849px;height:1101px;background:var(--paper);overflow:hidden}
.top-band{position:absolute;left:0;top:0;width:100%;height:45px;background:var(--sky)}
.top-strip{position:absolute;left:0;top:45px;width:100%;height:13px;background:var(--mist)}
.product-shot{position:absolute;left:37px;top:91px;width:366px;height:510px}
.features{position:absolute;left:427px;top:126px;width:372px;list-style:none}
.feature{position:absolute;left:0;width:372px}
.feature-icon{position:absolute;left:0;top:0;width:56px;height:60px}
.feature-title{position:absolute;left:84px;top:0;font-size:14px;font-weight:500;letter-spacing:.1px;white-space:nowrap}
.feature-body{position:absolute;left:84px;top:28px;width:288px;font-size:14px;font-weight:300;line-height:18.3px;color:var(--ink-soft);text-align:justify;text-align-last:left}
.promo-band{position:absolute;left:0;top:673px;width:100%;height:202px;background:var(--sun)}
.promo-point{position:absolute;font-size:18px;font-weight:300;line-height:21.6px;text-align:justify;text-align-last:left}
.promo-point .tick{position:absolute;left:-25px;top:3px;width:16px;height:16px}
.promo-left{left:75px;width:288px}
.promo-right{left:471px;width:328px}
.brand{position:absolute;left:49px;top:950px;display:flex;align-items:center;gap:12px}
.brand-mark{width:18px;height:18px;background:var(--ink)}
.brand-name{font-size:44px;font-weight:400;letter-spacing:2px;color:var(--ink)}
.call{position:absolute;left:371px;top:950px;width:200px;text-align:center}
.call-number{font-size:26px;font-weight:400;line-height:28px;white-space:nowrap}
.call-note{font-size:15px;font-weight:400;line-height:18px}
.divider{position:absolute;left:589px;top:961px;width:1.5px;height:51px;background:var(--ink)}
.contact{position:absolute;left:605px;top:956px;font-size:17px;font-weight:400;line-height:22px}
.bottom-band{position:absolute;left:0;top:1053px;width:100%;height:48px;background:var(--mist)}
</style>
</head>
<body>
<main class="flyer">
  <div class="top-band"></div>
  <div class="top-strip"></div>

  <svg class="product-shot" viewBox="0 0 366 510" role="img" aria-label="Product photo of an outdoor LED screen showing a child playing with a ball on grass">
    <defs>
      <linearGradient id="screenFill" x1="0" y1="0" x2="0" y2="1">
        <stop offset="0" stop-color="#b9c86a"/>
        <stop offset=".3" stop-color="#a9c04f"/>
        <stop offset=".7" stop-color="#b4c873"/>
        <stop offset="1" stop-color="#ffffff"/>
      </linearGradient>
      <linearGradient id="sideFill" x1="0" y1="0" x2="0" y2="1">
        <stop offset="0" stop-color="#000"/>
        <stop offset=".75" stop-color="#000"/>
        <stop offset="1" stop-color="#ffffff"/>
      </linearGradient>
    </defs>
    <polygon points="0,12 58,0 58,510 0,510" fill="url(#sideFill)"/>
    <polygon points="58,0 366,62 366,510 58,510" fill="url(#screenFill)"/>
  </svg>

  <ul class="features">
    <li class="feature" style="top:0">
      <svg class="feature-icon" viewBox="0 0 56 60" aria-hidden="true">
        <text x="0" y="44" font-family="Raleway, sans-serif" font-weight="500" font-size="30" fill="var(--icon)">4G</text>
        <path d="M40 16a8 8 0 0 1 6 10M42 9a14 14 0 0 1 10 18M44 3a20 20 0 0 1 12 26" fill="none" stroke="var(--icon)" stroke-width="2.6"/>
      </svg>
      <h2 class="feature-title">4G CAPABLE</h2>
      <p class="feature-body">Change screen content with a click of the mouse anywhere in the world</p>
    </li>
    <li class="feature" style="top:93px">
      <svg class="feature-icon" viewBox="0 0 56 60" aria-hidden="true">
        <path d="M2 24a38 38 0 0 1 52 0M10 33a26 26 0 0 1 36 0" fill="none" stroke="var(--icon)" stroke-width="5" stroke-linecap="round"/>
        <circle cx="28" cy="45" r="7" fill="var(--icon)"/>
      </svg>
      <h2 class="feature-title">WIFI CAPABLE</h2>
      <p class="feature-body">Change screen content with a PC, tablet or mobile phone an easy to use app</p>
    </li>
    <li class="feature" style="top:186px">
      <svg class="feature-icon" viewBox="0 0 56 60" aria-hidden="true">
        <g stroke="var(--icon)" stroke-width="3" stroke-linecap="round" fill="none">
          <circle cx="28" cy="30" r="9"/>
          <path d="M28 4v8M28 48v8M2 30h8M46 30h8M10 12l5 5M41 43l5 5M46 12l-5 5M15 43l-5 5"/>
        </g>
      </svg>
      <h2 class="feature-title">INTELIGENT BRIGHTNESS CONTROL</h2>
      <p class="feature-body">Screen will automatically adjust to suit ambiant light improving screen viewing quality and saving in power consumption</p>
    </li>
    <li class="feature" style="top:301px">
      <svg class="feature-icon" viewBox="0 0 56 60" aria-hidden="true">
        <g stroke="var(--icon)" stroke-width="1.8" fill="none">
          <rect x="10" y="22" width="36" height="24"/>
          <path d="M2 54h52l-6-8H8z"/>
          <rect x="30" y="2" width="6" height="32" rx="3" fill="var(--paper)"/>
          <circle cx="33" cy="38" r="5" fill="var(--icon)"/>
          <path d="M14 6v12M8 12h12M10 8l8 8M18 8l-8 8"/>
        </g>
      </svg>
      <h2 class="feature-title">ONLINE MONITORING</h2>
      <p class="feature-body">Monitor cabinet temperature and humidity plus more in real time online. Recieve alerts via email</p>
    </li>
    <li class="feature" style="top:412px">
      <svg class="feature-icon" viewBox="0 0 56 66" aria-hidden="true">
        <circle cx="28" cy="22" r="18" fill="var(--icon)"/>
        <path d="M28 12l3 7 7 .5-5.5 4.5 2 7-6.5-4-6.5 4 2-7-5.5-4.5 7-.5z" fill="var(--paper)"/>
        <path d="M20 42h16v20l-8 4-8-4z" fill="var(--icon)"/>
      </svg>
      <h2 class="feature-title">HIGH QUALITY PRODUCTS</h2>
      <p class="feature-body">Setting high standard for colour, brightness and sharpness these LED modules will create attention</p>
    </li>
  </ul>

  <section class="promo-band">
    <p class="promo-point promo-left" style="top:38px">
      <svg class="tick" viewBox="0 0 16 16" aria-hidden="true"><rect x="1.5" y="1.5" width="13" height="13" fill="none" stroke="var(--ink)" stroke-width="2"/><path d="M4 8l3 3 8-9" fill="none" stroke="var(--ink)" stroke-width="2.4"/></svg>
      Bring attnetion to your bussiness with your own hd led display.
    </p>
    <p class="promo-point promo-left" style="top:103px">
      <svg class="tick" viewBox="0 0 16 16" aria-hidden="true"><rect x="1.5" y="1.5" width="13" height="13" fill="none" stroke="var(--ink)" stroke-width="2"/><path d="M4 8l3 3 8-9" fill="none" stroke="var(--ink)" stroke-width="2.4"/></svg>
      our displays can be mounted outdoors on walls, roofs, xed signs, trailer mounted ect.
    </p>
    <p class="promo-point promo-right" style="top:38px">
      <svg class="tick" viewBox="0 0 16 16" aria-hidden="true"><rect x="1.5" y="1.5" width="13" height="13" fill="none" stroke="var(--ink)" stroke-width="2"/><path d="M4 8l3 3 8-9" fill="none" stroke="var(--ink)" stroke-width="2.4"/></svg>
      we also do indoor led screens for shop fronts and display stands.
    </p>
    <p class="promo-point promo-right" style="top:103px">
      <svg class="tick" viewBox="0 0 16 16" aria-hidden="true"><rect x="1.5" y="1.5" width="13" height="13" fill="none" stroke="var(--ink)" stroke-width="2"/><path d="M4 8l3 3 8-9" fill="none" stroke="var(--ink)" stroke-width="2.4"/></svg>
      All screens are custom built to your requirements including size, shape and even curved display
    </p>
  </section>

  <div class="brand">
    <span class="brand-mark"></span>
    <span class="brand-name">Zo Fen</span>
  </div>

  <div class="call">
    <p class="call-number">1300 555 019</p>
    <p class="call-note">for a free quote</p>
  </div>
  <div class="divider"></div>
  <div class="contact">
    <p>info@zofenscreens.com.au</p>
    <p>www.zofenscreens.com.au</p>
  </div>

  <div class="bottom-band"></div>
</main>
</body>
</html>
```